Start up business website

IT Support provider that caters towards law enforcement / police departments. We'll offer remote IT support, backup / recovery services and cyber security. Will add updates soon.

Target Market(s)

Police departments / Law Enforcement

Coding

Coded - Design and coding required

Number of Pages Required

5+ page

Font styles to use
Other font styles liked:
• Use font style in uploaded logo

Colors
0054AA
0677BA
7BADD7
CADEEF
E8F1F8

```html
<!DOCTYPE html>
<html lang="en">
<head>
<meta charset="utf-8">
<title>Bastion Support Services – Veteran Owned Security Services</title>
<link href="https://fonts.googleapis.com/css2?family=Roboto:wght@300;400;500;700&display=swap" rel="stylesheet">
<style>
:root{
  --blue:#0b56b0;
  --blue-mid:#1565c0;
  --blue-soft:#7badd7;
  --blue-pale:#e8f1f8;
  --red:#c8102e;
  --red-text:#e3213f;
  --dark:#333333;
  --ink:#222222;
  --muted:#666666;
  --faint:#9a9a9a;
  --grey-bg:#f2f2f2;
  --field:#f1f1f1;
  --white:#ffffff;
}
*{margin:0;padding:0;box-sizing:border-box}
html,body{width:1200px;height:3713px;overflow:hidden}
body{font-family:'Roboto',sans-serif;color:var(--ink);background:var(--white);position:relative}
.abs{position:absolute}

/* header */
.site-header{position:absolute;top:0;left:0;width:1200px;height:77px;background:var(--white);z-index:5}
.brand{position:absolute;left:76px;top:22px;display:flex;align-items:center;gap:10px;font-size:22px;font-weight:700;color:var(--blue)}
.brand-dot{width:32px;height:32px;border-radius:50%;background:var(--blue)}
.main-nav{position:absolute;top:30px;left:549px;font-size:13px;color:#444}
.main-nav a{position:absolute;white-space:nowrap;color:inherit;text-decoration:none}
.btn-contact{position:absolute;left:979px;top:16px;width:144px;height:47px;background:var(--blue);color:#fff;border-radius:4px;font-size:13px;font-weight:500;display:flex;align-items:center;justify-content:center}

/* hero */
.hero{position:absolute;top:77px;left:0;width:1200px;height:720px}
.hero-bg{position:absolute;top:0;left:0}
.hero-copy{position:absolute;left:76px;color:#fff}
.hero-kicker{top:160px;font-size:34px;font-weight:500}
.hero-title{top:198px;font-size:68px;font-weight:700;letter-spacing:-0.5px}
.hero-sub{top:290px;font-size:16px;font-weight:500}
.hero-rule{top:350px;width:52px;height:4px;background:#fff}
.hero-text{top:376px;width:520px;font-size:13px;line-height:26px}

.vet-badge{position:absolute;left:557px;top:595px;width:86px;height:86px;border-radius:50%;background:#fff;border:6px solid var(--red);box-shadow:0 3px 8px rgba(0,0,0,.2)}

/* quote card */
.quote-card{position:absolute;left:712px;top:107px;width:384px;height:696px;background:#fff;box-shadow:0 4px 18px rgba(0,0,0,.12);border-radius:3px;overflow:hidden;z-index:3}
.quote-call{height:76px;background:var(--dark);display:flex;align-items:center;padding-left:18px;color:#fff}
.call-icon{width:50px;height:50px;border-radius:50%;background:#4a4a4a;display:flex;align-items:center;justify-content:center;margin-right:20px}
.call-label{font-size:16px;line-height:21px}
.call-number{font-size:19px;font-weight:500;line-height:24px}
.quote-head{position:absolute;top:76px;left:0;width:384px}
.quote-title{position:absolute;top:14px;width:100%;text-align:center;color:#fff;font-size:33px;font-weight:500}
.quote-seal{position:absolute;top:170px;left:162px;width:60px;height:60px;border-radius:50%;background:#fff;border:3px solid var(--blue);box-shadow:0 2px 6px rgba(0,0,0,.2)}
.field{position:absolute;left:26px;width:333px;height:50px;background:var(--field);border-radius:3px;display:flex;align-items:center;padding-left:14px;font-size:13px;color:#b5b5b5}
.field svg{margin-right:12px;flex:none}
.field-area{height:102px;align-items:flex-start;padding-top:16px}
.field .chev{position:absolute;right:16px;top:19px}
.quote-submit{position:absolute;left:26px;top:607px;width:333px;height:58px;background:var(--blue);color:#fff;border-radius:3px;font-size:16px;font-weight:500;display:flex;align-items:center;justify-content:center}

/* why */
.why{position:absolute;top:720px;left:0;width:1200px;height:602px;background:var(--grey-bg)}
.section-title{position:absolute;width:1200px;text-align:center;color:var(--dark);font-weight:500}
.why-title{top:140px;font-size:37px;line-height:57px}
.feature{position:absolute;top:311px;width:246px;height:226px;background:#fff;box-shadow:0 3px 12px rgba(0,0,0,.08);padding:30px 24px}
.feature.is-active{background:var(--blue-mid);color:#fff}
.feature-title{margin-top:18px;font-size:17px;font-weight:500}
.feature-text{margin-top:14px;font-size:12px;line-height:30px;color:var(--muted)}
.feature.is-active .feature-text{color:#fff}

/* about */
.about-photo{position:absolute;left:76px;top:1409px;width:489px;height:458px;background:linear-gradient(135deg,#6f7d8f 0%,#2b2f36 55%,#1a1c20 100%)}
.about-copy{position:absolute;left:621px;top:1440px;width:470px}
.about-title{font-size:36px;font-weight:500;color:var(--dark)}
.about-rule{width:57px;height:3px;background:var(--blue);margin-top:10px}
.about-text{margin-top:26px;font-size:12px;line-height:26.2px;color:var(--muted)}
.about-sub{margin-top:30px;font-size:15px;font-weight:500;color:var(--dark)}
.checks{list-style:none;margin-top:16px}
.checks li{display:flex;align-items:center;font-size:12px;color:var(--muted);height:29.5px}
.checks svg{margin-right:19px}

/* services */
.services{position:absolute;top:1932px;left:0;width:1200px;height:488px;background:linear-gradient(90deg,#fafafa 0%,#f3f4f6 45%,#dde1e8 70%,#c9ced7 100%)}
.services-title{top:50px;font-size:37px}
.service{position:absolute;top:180px;width:300px;text-align:center}
.service-icon{width:104px;height:104px;border-radius:50%;background:#fff;margin:0 auto;box-shadow:0 3px 10px rgba(0,0,0,.1);display:flex;align-items:center;justify-content:center}
.service-name{margin-top:26px;font-size:16px;font-weight:500;color:var(--dark)}
.service-text{margin-top:12px;font-size:12px;line-height:26px;color:var(--muted)}

/* cta */
.cta{position:absolute;top:2420px;left:0;width:1200px;height:252px;background:var(--dark);color:#fff}
.cta-title{position:absolute;left:278px;top:72px;font-size:40px;font-weight:500}
.cta-call{position:absolute;left:278px;top:130px;font-size:28px;font-weight:500}
.cta-call span{color:var(--red-text)}
.cta-btn{position:absolute;left:875px;top:95px;width:211px;height:65px;background:var(--blue-mid);border-radius:3px;font-size:23px;font-weight:500;display:flex;align-items:center;justify-content:center}

/* testimonials */
.testimonials{position:absolute;top:2672px;left:0;width:1200px;height:617px;background:linear-gradient(180deg,#f2f2f2 0%,#ffffff 35%)}
.testi-title{top:40px;font-size:37px}
.testi-sub{position:absolute;top:111px;width:1200px;text-align:center;font-size:12px;color:var(--muted)}
.review{position:absolute;top:202px;width:453px;height:303px;background:#fff;box-shadow:0 3px 14px rgba(0,0,0,.08);padding:0 33px}
.review-head{position:relative;height:101px;border-bottom:1px solid #e3e3e3}
.avatar{position:absolute;left:0;top:21px;width:61px;height:61px;border-radius:50%;color:#fff;font-size:28px;font-weight:500;display:flex;align-items:center;justify-content:center}
.reviewer{position:absolute;left:82px;top:41px;font-size:15px;font-weight:500}
.stars{position:absolute;right:0;top:40px}
.review-text{margin-top:19px;font-size:12px;line-height:27.5px;color:var(--muted)}
.review-date{margin-top:24px;font-size:13px;color:#b3b3b3}
.arrow{position:absolute;top:345px}
.dots{position:absolute;top:555px;left:555px;display:flex;gap:16px}
.dots span{width:10px;height:10px;border-radius:50%;background:#d5d9e0}
.dots span.on{background:var(--blue-mid)}

/* quick contact */
.contact{position:absolute;top:3289px;left:0;width:1200px;height:424px}
.contact-panel{position:absolute;left:0;top:0;width:598px;height:424px;background:var(--blue-mid);color:#fff}
.contact-title{position:absolute;left:76px;top:44px;font-size:38px;font-weight:700}
.line-field{position:absolute;border-bottom:1px solid rgba(255,255,255,.85);font-size:11px;padding:0 0 7px 5px}
.contact-submit{position:absolute;left:157px;top:319px;width:333px;height:57px;background:#fff;color:var(--blue-mid);border-radius:3px;font-size:16px;font-weight:500;display:flex;align-items:center;justify-content:center}
.contact-map{position:absolute;left:598px;top:0;width:602px;height:424px;background:linear-gradient(135deg,#e9ecef 0%,#e4e7ea 50%,#d6e6f2 100%)}
</style>
</head>
<body>

<header class="site-header">
  <div class="brand"><span class="brand-dot"></span>Bastion</div>
  <nav class="main-nav">
    <a style="left:0">About us</a>
    <a style="left:104px">Services</a>
    <a style="left:188px">Follow Up</a>
    <a style="left:280px">CJIS Compliance</a>
  </nav>
  <div class="btn-contact">Contact Us</div>
</header>

<section class="hero">
  <svg class="hero-bg" width="1200" height="720" viewBox="0 0 1200 720">
    <defs>
      <linearGradient id="heroTone" x1="0" y1="0" x2="1" y2="1">
        <stop offset="0" stop-color="#1f5fb0"/>
        <stop offset=".5" stop-color="#1a56a6"/>
        <stop offset="1" stop-color="#1650a0"/>
      </linearGradient>
    </defs>
    <rect width="1200" height="720" fill="#f2f2f2"/>
    <polygon points="0,570 600,648 1200,530 1200,579 600,705 0,620" fill="var(--red)"/>
    <polygon points="0,0 1200,0 1200,530 600,648 0,522" fill="url(#heroTone)" role="img" aria-label="Photo of a security guard in cap and sunglasses under a blue overlay"/>
  </svg>
  <div class="hero-copy hero-kicker">Veteran owned</div>
  <div class="hero-copy hero-title">Security Services</div>
  <div class="hero-copy hero-sub">A Local, Independent and Quality Security comapny in The United States</div>
  <div class="hero-copy hero-rule"></div>
  <p class="hero-copy hero-text">Lorem ipsum dolor sit amet, consectetur adipisicing elit, sed do eiusmod tempor incididunt ut labore et dolore magna aliqua. Ut enim ad minim veniam, quis nostrud exercitation ullamco laboris nisi.</p>
</section>

<section class="why">
  <h2 class="section-title why-title">Why choose<br>Bastion Support Services</h2>

  <article class="feature" style="left:76px">
    <svg width="48" height="48" viewBox="0 0 48 48" fill="none" stroke="#222" stroke-width="2"><path d="M24 3l18 6v13c0 11-8 19-18 23C14 41 6 33 6 22V9z"/><circle cx="24" cy="24" r="11"/><path d="M18 27c2 2 4 3 6 3M20 19l2 3-2 2M27 20h4v6"/></svg>
    <h3 class="feature-title">Emergency Dispatch</h3>
    <p class="feature-text">We can have a security guard sent out in less than an hour.</p>
  </article>
  <article class="feature" style="left:343px">
    <svg width="48" height="48" viewBox="0 0 48 48" fill="none" stroke="#222" stroke-width="2"><path d="M24 3l18 6v13c0 11-8 19-18 23C14 41 6 33 6 22V9z"/><circle cx="24" cy="22" r="8"/><circle cx="24" cy="22" r="3"/><path d="M19 29l-3 8 4-2 2 3 2-6M29 29l3 8-4-2-2 3"/></svg>
    <h3 class="feature-title">Fair Wage</h3>
    <p class="feature-text">Our serurity guards are paid well to do the best job possible.</p>
  </article>
  <article class="feature is-active" style="left:611px">
    <svg width="48" height="48" viewBox="0 0 48 48" fill="none" stroke="#fff" stroke-width="2"><path d="M24 3l18 6v13c0 11-8 19-18 23C14 41 6 33 6 22V9z"/><circle cx="24" cy="19" r="7"/><path d="M24 15v8M12 30l6 3h8l6-4M12 30h-2"/></svg>
    <h3 class="feature-title">Affordable Prices</h3>
    <p class="feature-text">Security solutions tailored to your needs.</p>
  </article>
  <article class="feature" style="left:878px">
    <svg width="48" height="48" viewBox="0 0 48 48" fill="none" stroke="#222" stroke-width="2"><path d="M24 3l18 6v13c0 11-8 19-18 23C14 41 6 33 6 22V9z"/><path d="M17 24l5 5 10-10"/></svg>
    <h3 class="feature-title">Trusted</h3>
    <p class="feature-text">We are veteran owned company. Fully insured and bonded.</p>
  </article>
</section>

<div class="vet-badge" role="img" aria-label="Veteran owned business seal"></div>

<aside class="quote-card">
  <div class="quote-call">
    <div class="call-icon"><svg width="24" height="24" viewBox="0 0 24 24" fill="#9a9a9a"><path d="M6.6 10.8c1.4 2.8 3.8 5.1 6.6 6.6l2.2-2.2c.3-.3.7-.4 1-.2 1.1.4 2.3.6 3.6.6.6 0 1 .4 1 1V20c0 .6-.4 1-1 1C10.6 21 3 13.4 3 4c0-.6.4-1 1-1h3.5c.6 0 1 .4 1 1 0 1.3.2 2.5.6 3.6.1.3 0 .7-.2 1z"/></svg></div>
    <div><div class="call-label">Call us today:</div><div class="call-number">+1 555-010-4821</div></div>
  </div>
  <div class="quote-head">
    <svg width="384" height="150" viewBox="0 0 384 150"><polygon points="0,0 384,0 384,62 192,142 0,62" fill="var(--blue)"/></svg>
    <div class="quote-title">Request a Quote</div>
  </div>
  <div class="quote-seal"></div>

  <div class="field" style="top:238px"><svg width="16" height="16" viewBox="0 0 16 16" fill="none" stroke="#bbb"><circle cx="8" cy="5" r="3.5"/><path d="M1.5 15c0-4 3-6 6.5-6s6.5 2 6.5 6"/></svg>Your Name</div>
  <div class="field" style="top:298px"><svg width="16" height="16" viewBox="0 0 16 16" fill="none" stroke="#bbb"><rect x="2" y="4" width="8" height="11"/><rect x="10" y="8" width="5" height="7"/><path d="M4 7h4M4 10h4"/></svg>Business/Organisation</div>
  <div class="field" style="top:362px"><svg width="16" height="16" viewBox="0 0 16 16" fill="none" stroke="#bbb"><circle cx="8" cy="8" r="6.5"/><circle cx="8" cy="8" r="3"/></svg>Select Service<svg class="chev" width="12" height="12" viewBox="0 0 12 12" fill="none" stroke="#aaa"><path d="M2 4l4 4 4-4"/></svg></div>
  <div class="field" style="top:424px"><svg width="18" height="14" viewBox="0 0 18 14" fill="none" stroke="#bbb"><rect x="1" y="1" width="16" height="12"/><path d="M1 1l8 7 8-7"/></svg>Your Email</div>
  <div class="field field-area" style="top:486px"><svg width="16" height="16" viewBox="0 0 16 16" fill="none" stroke="#bbb"><circle cx="8" cy="8" r="6.5"/><path d="M8 7v5M8 4.5v.5"/></svg>Request</div>
  <div class="quote-submit">SUBMIT NOW</div>
</aside>

<section>
  <div class="about-photo" role="img" aria-label="Photo of a security officer seen from behind watching a crowd at an outdoor event"></div>
  <div class="about-copy">
    <h2 class="about-title">About Us</h2>
    <div class="about-rule"></div>
    <p class="about-text">Lorem ipsum dolor sit amet, consectetur adipisicing elit, sed do eiusmod tempor incididunt ut labore et dolore magna aliqua. Ut enim ad minim veniam, quis nostrud exercitation ullamco laboris nisi ut aliquip ex ea commodo consequat. Duis aute irure dolor in reprehenderit in voluptate velit esse cillum dolore eu fugiat nulla pariatur. Excepteur sint occaecat cupidatat non proident, sunt in culpa qui officia deserunt mollit anim id est laborum.</p>
    <h3 class="about-sub">Lorem Ipsum dolor Sit</h3>
    <ul class="checks">
      <li><svg width="18" height="18" viewBox="0 0 18 18"><circle cx="9" cy="9" r="9" fill="var(--blue-mid)"/><path d="M5 9.5l2.7 2.5L13 6.5" fill="none" stroke="#fff" stroke-width="2"/></svg>Lorem ipsum dolor sit amet, consectetur adipisicing elit, sed do</li>
      <li><svg width="18" height="18" viewBox="0 0 18 18"><circle cx="9" cy="9" r="9" fill="var(--blue-mid)"/><path d="M5 9.5l2.7 2.5L13 6.5" fill="none" stroke="#fff" stroke-width="2"/></svg>Lorem ipsum dolor sit amet, consectetur adipisicing elit, sed do</li>
      <li><svg width="18" height="18" viewBox="0 0 18 18"><circle cx="9" cy="9" r="9" fill="var(--blue-mid)"/><path d="M5 9.5l2.7 2.5L13 6.5" fill="none" stroke="#fff" stroke-width="2"/></svg>Lorem ipsum dolor sit amet, consectetur adipisicing elit, sed do</li>
    </ul>
  </div>
</section>

<section class="services" role="img" aria-label="Faded photo of a security officer in cap and sunglasses behind the services list">
  <h2 class="section-title services-title">Services we offer</h2>
  <div class="service" style="left:85px">
    <div class="service-icon"><svg width="56" height="56" viewBox="0 0 56 56" fill="none" stroke="var(--blue-mid)" stroke-width="2.5"><circle cx="28" cy="28" r="9"/><path d="M28 6l4 5 6-2 1 6 6 1-2 6 5 4-5 4 2 6-6 1-1 6-6-2-4 5-4-5-6 2-1-6-6-1 2-6-5-4 5-4-2-6 6-1 1-6 6 2z"/></svg></div>
    <h3 class="service-name">IT Support</h3>
    <p class="service-text">Lorem ipsum dolor sit amet, consectetur<br>adipisicing elit, sed do eiusmod</p>
  </div>
  <div class="service" style="left:450px">
    <div class="service-icon"><svg width="52" height="52" viewBox="0 0 52 52" fill="none" stroke="var(--blue-mid)" stroke-width="2.5"><ellipse cx="26" cy="12" rx="15" ry="5"/><path d="M11 12v28c0 3 7 5 15 5s15-2 15-5V12M11 26c0 3 7 5 15 5s15-2 15-5"/></svg></div>
    <h3 class="service-name">Backup/Recovery</h3>
    <p class="service-text">Lorem ipsum dolor sit amet, consectetur<br>adipisicing elit, sed do eiusmod</p>
  </div>
  <div class="service" style="left:815px">
    <div class="service-icon"><svg width="58" height="58" viewBox="0 0 58 58" fill="none" stroke="var(--blue-mid)" stroke-width="2.5"><circle cx="29" cy="29" r="23"/><ellipse cx="29" cy="29" rx="10" ry="23"/><path d="M6 29h46M10 17h38M10 41h38M29 6v46"/></svg></div>
    <h3 class="service-name">Cyber Security</h3>
    <p class="service-text">Lorem ipsum dolor sit amet, consectetur<br>adipisicing elit, sed do eiusmod</p>
  </div>
</section>

<section class="cta">
  <h2 class="cta-title">Need Security Services?</h2>
  <p class="cta-call">Call : <span>+1 555-014-2290</span></p>
  <div class="cta-btn">Get a Quote</div>
</section>

<section class="testimonials">
  <h2 class="section-title testi-title">Testimonials</h2>
  <p class="testi-sub">Don't take our word for it, see what our clients have to say about it</p>

  <svg class="arrow" style="left:76px" width="30" height="16" viewBox="0 0 30 16" fill="none" stroke="#222" stroke-width="2"><path d="M29 8H2M9 1L2 8l7 7"/></svg>

  <article class="review" style="left:127px">
    <div class="review-head">
      <div class="avatar" style="background:#f28b8b">M</div>
      <div class="reviewer">Maren Cole</div>
      <svg class="stars" width="94" height="16" viewBox="0 0 94 16" fill="#f5b400"><g id="star"><path d="M8 0l2.4 5.2 5.6.6-4.2 3.8 1.2 5.6L8 12.4 3 15.2l1.2-5.6L0 5.8l5.6-.6z"/></g><use href="#star" x="19.5"/><use href="#star" x="39"/><use href="#star" x="58.5"/><use href="#star" x="78"/></svg>
    </div>
    <p class="review-text">Lorem ipsum dolor sit amet, consectetur adipisicing elit, sed do eiusmod tempor incididunt ut labore et dolore magna aliqua.<br>&nbsp;Ut enim ad minim veniam, quis nostrud exercitation ullamco laboris nisi ut aliquip ex ea commodo consequat.</p>
    <p class="review-date">August 13, 2021</p>
  </article>

  <article class="review" style="left:619px">
    <div class="review-head">
      <div class="avatar" style="background:#8ed0f2">D</div>
      <div class="reviewer">Dana Pruitt</div>
      <svg class="stars" width="94" height="16" viewBox="0 0 94 16" fill="#f5b400"><use href="#star"/><use href="#star" x="19.5"/><use href="#star" x="39"/><use href="#star" x="58.5"/><use href="#star" x="78"/></svg>
    </div>
    <p class="review-text">Lorem ipsum dolor sit amet, consectetur adipisicing elit, sed do eiusmod tempor incididunt ut labore et dolore magna aliqua.<br>&nbsp;Ut enim ad minim veniam, quis nostrud exercitation ullamco laboris nisi ut aliquip ex ea commodo consequat.</p>
    <p class="review-date">August 13, 2021</p>
  </article>

  <svg class="arrow" style="left:1094px" width="30" height="16" viewBox="0 0 30 16" fill="none" stroke="#222" stroke-width="2"><path d="M1 8h27M21 1l7 7-7 7"/></svg>

  <div class="dots"><span class="on"></span><span></span><span></span><span></span></div>
</section>

<section class="contact">
  <div class="contact-panel">
    <h2 class="contact-title">Quick Contact</h2>
    <div class="line-field" style="left:76px;top:142px;width:235px">Name</div>
    <div class="line-field" style="left:334px;top:142px;width:237px">Email Address</div>
    <div class="line-field" style="left:76px;top:204px;width:495px">Subject</div>
    <div class="line-field" style="left:76px;top:257px;width:495px">Your Message</div>
    <div class="contact-submit">SUBMIT NOW</div>
  </div>
  <div class="contact-map" role="img" aria-label="Street map showing the office location"></div>
</section>

</body>
</html>
```